Platesafe Card for Healthy Restaurant Dining

I am seeking a design for a physical card to communicate my wife's health-related dietary restriction regarding seed oils. This card will be given to restaurant waiters to ensure her meals are prepared without seed oils, as it is a health issue and not merely a preference.
My wife cannot eat any “seed oil” or “processed oil”, including:
- Vegetable oil
- Canola oil
- Soybean oil
- Sunflower oil
- Corn oil
- Cottonseed oil
- Safflower oil
- Peanut oil
- Sesame oil
Oils that are OK for her to consume:
- Butter (most preferable)
- Extra virgin olive oil
- Avocado oil
- Coconut oil
- Ghee
- Lard
- Any other animal-based fats
Key Design Requirements:
- Clarity and speed of communication: The card should be easily read and understood by waiters, even in low-light environments, emphasizing that it's a health concern.
- Avoid common misconceptions: Ensure the design doesn't imply common dietary preferences like "vegetarian" or "no butter." Animal fats and butter are actually preferable for her!
- Preferred term: Use "seed oils" as the term to describe what she cannot eat due to her health issue.
- Trace amounts are acceptable: Communicate that it's OK to use cookware that has previously been in contact with seed oils, but not to have seed oil as an ingredient. Please suggest a concise way to convey this.
- Card dimensions: Design should be 3.5” x 2.25” (standard credit-card size on cardlora-print.test). Horizontal or vertical layouts are both fine, whichever makes the message clearer.
Design Suggestions:
- Utilize bold and easy-to-read typography to communicate the main message.
- Consider incorporating relevant icons or graphics that help convey the message without adding confusion.
- Use contrasting colors to enhance readability, especially in low-light situations.
- To communicate the “trace amounts OK” part, consider phrases such as:
- "Cross-contamination acceptable"
- “Used cookware OK, no ingredient use”
- “Separate cookware not necessary”
Thank you for your assistance in creating this essential card for my wife's health and safety when dining out!

```html
<!DOCTYPE html>
<html lang="en">
<head>
<meta charset="utf-8">
<title>Platesafe Card</title>
<link rel="stylesheet" href="https://fonts.googleapis.com/css2?family=Open+Sans:ital,wght@0,400;0,600;0,700;1,400&display=swap">
<style>
  :root {
    --page: #e1e2e4;
    --card: #ffffff;
    --brand-blue: #1a6db3;
    --alert-red: #c8242d;
    --safe-green: #3b8b3d;
    --ink: #1f1f1f;
    --faint: #d9dbde;
    --sheen: #eef0f3;
  }
  * { box-sizing: border-box; margin: 0; padding: 0; }
  html, body { width: 1200px; height: 2742px; overflow: hidden; }
  body {
    background: var(--page);
    font-family: "Open Sans", Arial, sans-serif;
    position: relative;
  }
  .card {
    position: absolute;
    top: 313px;
    width: 514px;
    height: 800px;
    border-radius: 26px;
    overflow: hidden;
    background: var(--card);
    box-shadow: 0 14px 22px rgba(0,0,0,0.28);
  }
  .card--front { left: 72px; }
  .card--back { left: 626px; }
  .card__sheen {
    position: absolute; inset: 0;
    background: linear-gradient(160deg, var(--sheen) 0%, #ffffff 35%, var(--sheen) 60%, #ffffff 85%, var(--sheen) 100%);
  }
  .front__header {
    position: absolute; left: 0; top: 0; width: 100%; height: 109px;
    background: var(--brand-blue); color: #fff; text-align: center;
  }
  .front__eyebrow { position: absolute; top: 18px; width: 100%; font-size: 29px; letter-spacing: 6px; font-weight: 400; }
  .front__title { position: absolute; top: 52px; width: 100%; font-size: 35px; font-weight: 700; letter-spacing: 0.2px; }
  .front__divider { position: absolute; left: 256px; top: 147px; width: 4px; height: 508px; background: var(--brand-blue); }
  .status-icon { position: absolute; top: 145px; width: 60px; height: 60px; }
  .status-icon--no { left: 98px; }
  .status-icon--ok { left: 355px; }
  .column__heading {
    position: absolute; top: 218px; width: 240px; text-align: center;
    font-size: 25px; line-height: 28px; font-weight: 600; color: var(--ink); letter-spacing: 0.3px;
  }
  .column__heading--no { left: 10px; }
  .column__heading--ok { left: 266px; }
  .oil-list { position: absolute; top: 326px; list-style: none; font-size: 28px; line-height: 35px; }
  .oil-list--no { left: 18px; color: var(--alert-red); }
  .oil-list--ok { left: 272px; color: var(--safe-green); }
  .oil-list li { position: relative; padding-left: 30px; white-space: nowrap; }
  .oil-list svg { position: absolute; left: 0; top: 9px; width: 21px; height: 21px; }
  .front__note {
    position: absolute; left: 28px; top: 672px; font-style: italic; font-size: 22px; line-height: 26px; color: var(--ink);
  }
  .front__note span { display: block; padding-left: 10px; }
  .front__footer {
    position: absolute; left: 0; bottom: 0; width: 100%; height: 51px; background: var(--brand-blue);
    color: #fff; text-align: center; font-size: 17px; font-weight: 700; letter-spacing: 2.6px; line-height: 51px;
  }
  .back__title {
    position: absolute; top: 372px; width: 100%; text-align: center;
    color: var(--brand-blue); font-size: 48px; font-weight: 600; line-height: 56px;
  }
  .back__url {
    position: absolute; top: 745px; width: 100%; text-align: center; color: var(--brand-blue);
    font-size: 24px; font-weight: 600; letter-spacing: 2px;
  }
</style>
</head>
<body>
  <section class="card card--front">
    <div class="card__sheen" role="img" aria-label="Soft white satin fabric background"></div>
    <header class="front__header">
      <div class="front__eyebrow">MEDICAL</div>
      <div class="front__title">DIETARY RESTRICTION</div>
    </header>

    <svg class="status-icon status-icon--no" viewBox="0 0 60 60" aria-hidden="true">
      <circle cx="30" cy="30" r="30" fill="#c8242d"/>
      <path d="M19 19 L41 41 M41 19 L19 41" stroke="#fff" stroke-width="7" stroke-linecap="round"/>
    </svg>
    <svg class="status-icon status-icon--ok" viewBox="0 0 60 60" aria-hidden="true">
      <circle cx="30" cy="30" r="30" fill="#3b8b3d"/>
      <path d="M16 31 L26 41 L45 21" fill="none" stroke="#fff" stroke-width="7" stroke-linecap="round" stroke-linejoin="round"/>
    </svg>

    <div class="column__heading column__heading--no">I CANNOT EAT:<br>PROCESSED<br>SEED OILS</div>
    <div class="column__heading column__heading--ok">ACCEPTABLE:<br>NATURAL OILS<br>AND FATS</div>

    <div class="front__divider"></div>

    <ul class="oil-list oil-list--no">
      <li><svg viewBox="0 0 20 20" aria-hidden="true"><circle cx="10" cy="10" r="8.5" fill="none" stroke="currentColor" stroke-width="1.8"/><path d="M6.5 6.5 L13.5 13.5 M13.5 6.5 L6.5 13.5" stroke="currentColor" stroke-width="1.8"/></svg>Vegetable oil</li>
      <li><svg viewBox="0 0 20 20" aria-hidden="true"><circle cx="10" cy="10" r="8.5" fill="none" stroke="currentColor" stroke-width="1.8"/><path d="M6.5 6.5 L13.5 13.5 M13.5 6.5 L6.5 13.5" stroke="currentColor" stroke-width="1.8"/></svg>Canola oil</li>
      <li><svg viewBox="0 0 20 20" aria-hidden="true"><circle cx="10" cy="10" r="8.5" fill="none" stroke="currentColor" stroke-width="1.8"/><path d="M6.5 6.5 L13.5 13.5 M13.5 6.5 L6.5 13.5" stroke="currentColor" stroke-width="1.8"/></svg>Soybean oil</li>
      <li><svg viewBox="0 0 20 20" aria-hidden="true"><circle cx="10" cy="10" r="8.5" fill="none" stroke="currentColor" stroke-width="1.8"/><path d="M6.5 6.5 L13.5 13.5 M13.5 6.5 L6.5 13.5" stroke="currentColor" stroke-width="1.8"/></svg>Sunflower oil</li>
      <li><svg viewBox="0 0 20 20" aria-hidden="true"><circle cx="10" cy="10" r="8.5" fill="none" stroke="currentColor" stroke-width="1.8"/><path d="M6.5 6.5 L13.5 13.5 M13.5 6.5 L6.5 13.5" stroke="currentColor" stroke-width="1.8"/></svg>Corn oil</li>
      <li><svg viewBox="0 0 20 20" aria-hidden="true"><circle cx="10" cy="10" r="8.5" fill="none" stroke="currentColor" stroke-width="1.8"/><path d="M6.5 6.5 L13.5 13.5 M13.5 6.5 L6.5 13.5" stroke="currentColor" stroke-width="1.8"/></svg>Cottonseed oil</li>
      <li><svg viewBox="0 0 20 20" aria-hidden="true"><circle cx="10" cy="10" r="8.5" fill="none" stroke="currentColor" stroke-width="1.8"/><path d="M6.5 6.5 L13.5 13.5 M13.5 6.5 L6.5 13.5" stroke="currentColor" stroke-width="1.8"/></svg>Safflower oil</li>
      <li><svg viewBox="0 0 20 20" aria-hidden="true"><circle cx="10" cy="10" r="8.5" fill="none" stroke="currentColor" stroke-width="1.8"/><path d="M6.5 6.5 L13.5 13.5 M13.5 6.5 L6.5 13.5" stroke="currentColor" stroke-width="1.8"/></svg>Peanut oil</li>
      <li><svg viewBox="0 0 20 20" aria-hidden="true"><circle cx="10" cy="10" r="8.5" fill="none" stroke="currentColor" stroke-width="1.8"/><path d="M6.5 6.5 L13.5 13.5 M13.5 6.5 L6.5 13.5" stroke="currentColor" stroke-width="1.8"/></svg>Sesame oil</li>
    </ul>

    <ul class="oil-list oil-list--ok">
      <li><svg viewBox="0 0 20 20" aria-hidden="true"><circle cx="10" cy="10" r="8.5" fill="none" stroke="currentColor" stroke-width="1.8"/><path d="M6 10.3 L8.8 13 L14 7.2" fill="none" stroke="currentColor" stroke-width="1.8"/></svg>Butter</li>
      <li><svg viewBox="0 0 20 20" aria-hidden="true"><circle cx="10" cy="10" r="8.5" fill="none" stroke="currentColor" stroke-width="1.8"/><path d="M6 10.3 L8.8 13 L14 7.2" fill="none" stroke="currentColor" stroke-width="1.8"/></svg>Extra virgin<br>olive oil</li>
      <li><svg viewBox="0 0 20 20" aria-hidden="true"><circle cx="10" cy="10" r="8.5" fill="none" stroke="currentColor" stroke-width="1.8"/><path d="M6 10.3 L8.8 13 L14 7.2" fill="none" stroke="currentColor" stroke-width="1.8"/></svg>Avocado oil</li>
      <li><svg viewBox="0 0 20 20" aria-hidden="true"><circle cx="10" cy="10" r="8.5" fill="none" stroke="currentColor" stroke-width="1.8"/><path d="M6 10.3 L8.8 13 L14 7.2" fill="none" stroke="currentColor" stroke-width="1.8"/></svg>Coconut oil</li>
      <li><svg viewBox="0 0 20 20" aria-hidden="true"><circle cx="10" cy="10" r="8.5" fill="none" stroke="currentColor" stroke-width="1.8"/><path d="M6 10.3 L8.8 13 L14 7.2" fill="none" stroke="currentColor" stroke-width="1.8"/></svg>Ghee</li>
      <li><svg viewBox="0 0 20 20" aria-hidden="true"><circle cx="10" cy="10" r="8.5" fill="none" stroke="currentColor" stroke-width="1.8"/><path d="M6 10.3 L8.8 13 L14 7.2" fill="none" stroke="currentColor" stroke-width="1.8"/></svg>Lard</li>
      <li><svg viewBox="0 0 20 20" aria-hidden="true"><circle cx="10" cy="10" r="8.5" fill="none" stroke="currentColor" stroke-width="1.8"/><path d="M6 10.3 L8.8 13 L14 7.2" fill="none" stroke="currentColor" stroke-width="1.8"/></svg>Natural animal<br>fats</li>
    </ul>

    <p class="front__note">*Trace amounts acceptable<span>Reused cookware acceptable</span></p>
    <footer class="front__footer">THANK YOU FOR KEEPING ME SAFE</footer>
  </section>

  <section class="card card--back">
    <div class="card__sheen" role="img" aria-label="Soft white satin fabric background"></div>
    <h1 class="back__title">Platesafe Card</h1>
    <p class="back__url">WWW.PLATESAFECARD.TEST</p>
  </section>
</body>
</html>
```